Commercial printing and sign company printed advertisement.

We're wanting a new look for our printed advertisements. We've been in business for 40 years and have been pushing hard the last couple of years to grow our business. Our target market is changing and our client base is changing. I am looking for advertisement that appeals to larger companies. However, we are not stuffy people so I would like the ads to convey our professionalism but also stand out with color and have a fun side. I'm currently needing advertisements for a printed magazine, printed newspaper, web ads and a table top at a local restaurant. We have our traditional four color logo (swoosh) as well as a simpler single color option. I am attaching various ads we have done previously so you can see what we have. It is important for these ads to convey the different things we do - as we do alot!

```html
<!DOCTYPE html>
<html lang="en">
<head>
<meta charset="utf-8">
<title>Brightline Printing – Why Shop Any Else?</title>
<link href="https://fonts.googleapis.com/css2?family=Playball&family=Roboto:ital,wght@0,400;0,500;0,700;0,900;1,500&display=swap" rel="stylesheet">
<style>
  :root {
    --navy: #1c2456;
    --blue: #0a8fd6;
    --purple: #7e3c98;
    --violet: #8a4cab;
    --magenta: #c2478d;
    --pink: #d9488a;
    --yellow: #f5e400;
    --gold: #ecd23a;
    --white: #ffffff;
    --brand-red: #d8232f;
  }
  * { margin: 0; padding: 0; box-sizing: border-box; }
  html, body { width: 848px; height: 1200px; overflow: hidden; background: #fff; }
  .ad {
    position: relative; width: 848px; height: 1200px; overflow: hidden;
    font-family: "Roboto", sans-serif; color: var(--white);
    background: linear-gradient(180deg, var(--navy) 0%, #2b3f8a 22%, #6a4fa1 34%, var(--violet) 55%, var(--purple) 72%, #a04a94 84%, #d7a35a 93%, var(--gold) 100%);
  }
  .hero-photo {
    position: absolute; left: 0; top: 0; width: 848px; height: 330px;
    background: linear-gradient(160deg, #1a1f4a 0%, #2c3a78 45%, #40508f 70%, #5a4f9c 100%);
  }
  .hero-band {
    position: absolute; left: 0; top: 237px; width: 848px; height: 90px;
    background: linear-gradient(90deg, #0a9be0 0%, var(--blue) 40%, #3d69b8 75%, #5a56a8 100%);
  }
  .brand {
    position: absolute; left: 40px; top: 60px;
    display: flex; align-items: center; gap: 10px;
  }
  .brand-square { width: 22px; height: 22px; background: var(--brand-red); }
  .brand-name { font-size: 32px; font-weight: 900; color: var(--white); }
  .headline {
    position: absolute; left: 380px; top: 60px; width: 440px;
    font-family: "Playball", cursive; line-height: 0.95;
  }
  .headline .line1 { display: block; font-size: 78px; color: var(--yellow); padding-left: 22px; }
  .headline .line2 { display: block; font-size: 78px; color: var(--white); }
  .tagline {
    position: absolute; left: 330px; top: 242px; width: 480px; text-align: center;
    font-size: 34px; font-style: italic; font-weight: 500; line-height: 1.08;
  }
  .shirt-photo {
    position: absolute; left: 590px; top: 335px; width: 258px; height: 445px;
  }
  .services { position: absolute; top: 388px; left: 32px; width: 760px; }
  .service {
    position: absolute; display: flex; align-items: center;
    font-size: 27px; font-weight: 700; height: 32px; white-space: nowrap;
  }
  .service::before {
    content: ""; position: absolute; left: 6px; top: 0; height: 32px; width: 280px;
    background: linear-gradient(90deg, rgba(255,255,255,0.18), rgba(255,255,255,0));
  }
  .service .dot {
    width: 11px; height: 11px; border-radius: 50%; background: var(--yellow);
    border: 2px solid var(--white); margin-right: 8px; position: relative;
  }
  .service .label { position: relative; }
  .service .more { font-size: 19px; font-weight: 400; margin-left: 8px; position: relative; }
  .anniversary { position: absolute; left: 38px; top: 796px; width: 300px; height: 220px; }
  .years-figure {
    position: absolute; left: 10px; top: 0; font-size: 190px; font-weight: 900;
    line-height: 1; letter-spacing: -12px;
    background: linear-gradient(180deg, #ffffff 30%, #c3a2dd 100%);
    -webkit-background-clip: text; background-clip: text; color: transparent;
  }
  .years-ribbon {
    position: absolute; left: 160px; top: 70px; width: 130px; height: 40px;
    background: var(--white); clip-path: polygon(0 0, 100% 0, 92% 50%, 100% 100%, 0 100%);
    color: var(--purple); font-size: 32px; font-weight: 900; padding-left: 12px; line-height: 40px;
  }
  .experience {
    position: absolute; left: 12px; top: 165px; font-size: 40px; font-weight: 700;
    border-bottom: 3px solid var(--yellow); padding-bottom: 2px;
  }
  .dot-grid { position: absolute; left: 303px; top: 963px; }
  .products-photo { position: absolute; left: 400px; top: 792px; width: 420px; height: 340px; }
  .ask-band {
    position: absolute; left: 0; top: 1046px; width: 640px; height: 55px;
    background: linear-gradient(90deg, rgba(217,72,138,0.55) 0%, var(--pink) 45%, var(--pink) 100%);
  }
  .ask-line {
    position: absolute; left: 38px; top: 1048px; font-family: "Playball", cursive;
    font-size: 40px; color: var(--white);
  }
  .contact { position: absolute; display: flex; align-items: center; gap: 10px; font-size: 17px; font-weight: 700; }
  .contact svg { width: 18px; height: 18px; flex: none; }
</style>
</head>
<body>
<main class="ad">
  <div class="hero-photo" role="img" aria-label="Photo of a large-format printer in operation"></div>
  <div class="hero-band"></div>

  <div class="brand">
    <span class="brand-square"></span>
    <span class="brand-name">Brightline Printing</span>
  </div>

  <h1 class="headline">
    <span class="line1">Why Shop</span>
    <span class="line2">Any Else?</span>
  </h1>
  <p class="tagline">When One Stop, One Shop,<br>Doing It All!</p>

  <svg class="shirt-photo" viewBox="0 0 258 445" role="img" aria-label="Photo of a blue T-shirt being screen printed, framed by a paint splash">
    <defs>
      <linearGradient id="shirtFill" x1="0" y1="0" x2="1" y2="1">
        <stop offset="0" stop-color="#e8e6ea"/>
        <stop offset="0.45" stop-color="#9a98a6"/>
        <stop offset="0.6" stop-color="#1f4f9a"/>
        <stop offset="1" stop-color="#143a78"/>
      </linearGradient>
    </defs>
    <path d="M80 20 C130 0 200 10 258 0 L258 445 C220 420 170 410 140 380 C100 350 60 330 30 280 C0 230 30 180 50 140 C70 100 40 60 80 20 Z" fill="url(#shirtFill)" stroke="#f5e400" stroke-width="3"/>
  </svg>

  <ul class="services">
    <li class="service" style="left:0;top:0"><span class="dot"></span><span class="label">Full Color Printing</span></li>
    <li class="service" style="left:0;top:40px"><span class="dot"></span><span class="label">Blue Prints</span></li>
    <li class="service" style="left:0;top:84px"><span class="dot"></span><span class="label">Color Copies</span></li>
    <li class="service" style="left:0;top:126px"><span class="dot"></span><span class="label">Signs of All Kinds</span></li>
    <li class="service" style="left:0;top:166px"><span class="dot"></span><span class="label">Wide Format Printing</span></li>
    <li class="service" style="left:0;top:209px"><span class="dot"></span><span class="label">Banners</span></li>
    <li class="service" style="left:0;top:251px"><span class="dot"></span><span class="label">Fleet Graphics</span></li>
    <li class="service" style="left:0;top:295px"><span class="dot"></span><span class="label">Invitations</span></li>
    <li class="service" style="left:0;top:335px"><span class="dot"></span><span class="label">Mailing Services</span></li>
    <li class="service" style="left:300px;top:0"><span class="dot"></span><span class="label">Promo Items</span></li>
    <li class="service" style="left:300px;top:40px"><span class="dot"></span><span class="label">Laminating</span></li>
    <li class="service" style="left:300px;top:84px"><span class="dot"></span><span class="label">Screen Printing</span></li>
    <li class="service" style="left:300px;top:126px"><span class="dot"></span><span class="label">Pens</span></li>
    <li class="service" style="left:300px;top:166px"><span class="dot"></span><span class="label">Political Signs</span></li>
    <li class="service" style="left:300px;top:209px"><span class="dot"></span><span class="label">Self-linking Stamps</span></li>
    <li class="service" style="left:300px;top:249px"><span class="dot"></span><span class="label">Post Cards</span></li>
    <li class="service" style="left:300px;top:293px"><span class="dot"></span><span class="label">Posters</span></li>
    <li class="service" style="left:300px;top:333px"><span class="dot"></span><span class="label">Embroidery</span><span class="more">And Much, Much More!</span></li>
  </ul>

  <div class="anniversary">
    <div class="years-figure">40</div>
    <div class="years-ribbon">YEARS</div>
    <div class="experience">Experience</div>
  </div>

  <svg class="dot-grid" width="76" height="40" viewBox="0 0 76 40" aria-hidden="true">
    <g fill="rgba(255,255,255,0.45)">
      <circle cx="4" cy="4" r="3"/><circle cx="16" cy="4" r="3"/><circle cx="28" cy="4" r="3"/><circle cx="40" cy="4" r="3"/><circle cx="52" cy="4" r="3"/><circle cx="64" cy="4" r="3"/>
      <circle cx="4" cy="16" r="3"/><circle cx="16" cy="16" r="3"/><circle cx="28" cy="16" r="3"/><circle cx="40" cy="16" r="3"/><circle cx="52" cy="16" r="3"/><circle cx="64" cy="16" r="3"/>
      <circle cx="4" cy="28" r="3"/><circle cx="16" cy="28" r="3"/><circle cx="28" cy="28" r="3"/><circle cx="40" cy="28" r="3"/><circle cx="52" cy="28" r="3"/><circle cx="64" cy="28" r="3"/>
    </g>
  </svg>

  <div class="products-photo" role="img" aria-label="Illustration of a wide-format printer with a colorful floral print, surrounded by promotional products: pens, bottles, tote bag, umbrella and paint splashes"
       style="background: radial-gradient(ellipse at 55% 45%, #4a5a7a 0%, #3a4868 35%, rgba(138,76,171,0) 70%);"></div>

  <div class="ask-band"></div>
  <p class="ask-line">Don’t See It? … Just Ask?</p>

  <div class="contact" style="left:42px;top:1115px">
    <svg viewBox="0 0 24 24" aria-hidden="true"><path d="M6.6 10.8a15 15 0 0 0 6.6 6.6l2.2-2.2a1 1 0 0 1 1-.25 11.4 11.4 0 0 0 3.6.6 1 1 0 0 1 1 1V20a1 1 0 0 1-1 1A17 17 0 0 1 3 4a1 1 0 0 1 1-1h3.5a1 1 0 0 1 1 1c0 1.25.2 2.45.6 3.6a1 1 0 0 1-.25 1z" fill="#fff"/></svg>
    <span>(555) 014-2290</span>
  </div>
  <div class="contact" style="left:42px;top:1143px">
    <svg viewBox="0 0 24 24" aria-hidden="true"><g fill="none" stroke="#fff" stroke-width="2"><circle cx="12" cy="12" r="9"/><path d="M3 12h18M12 3c3 3 3 15 0 18M12 3c-3 3-3 15 0 18"/></g></svg>
    <span>www.brightlineprint.com</span>
  </div>
  <div class="contact" style="left:282px;top:1115px">
    <svg viewBox="0 0 24 24" aria-hidden="true"><g fill="none" stroke="#fff" stroke-width="2"><rect x="2" y="5" width="20" height="14"/><path d="M2 5l10 8 10-8"/></g></svg>
    <span>art@brightlineprint.com</span>
  </div>
  <div class="contact" style="left:282px;top:1143px">
    <svg viewBox="0 0 24 24" aria-hidden="true"><path d="M12 2a7 7 0 0 0-7 7c0 5 7 13 7 13s7-8 7-13a7 7 0 0 0-7-7zm0 9.5A2.5 2.5 0 1 1 12 6.5a2.5 2.5 0 0 1 0 5z" fill="#fff"/></svg>
    <span>215 W Main Street, Maple Ridge, Missouri</span>
  </div>
</main>
</body>
</html>
```